Bref créative
Complete Stationery Project for KMT
KMT - Real Estate Agency and Education Centre
I need double sided standard sized Business Card [3.5" x 2"]
Fonts and tag lines remain same font. Other texts, we're open to ideas from designers
Simple
Hendra Wiratmo
Owner / Realtor
Wisma Cakra Baruna 11 Floor
Jl. Raya Pemuda Kav. 3-4
Pasir Melati - Kebon Sirih
Jakarta Pusat - 10390
hendrawira@mailbox-example.com
www.hendra-wiratmo-example.com
K98765432
We require 2 different designs for 2 different companies. One is a real estate agency, the other is an education centre which provides courses in real estate, sales, motivation and personal development.
For the real estate agency:
- Name of company is P.T. Kirana Maju Teguh
- logo used shall be without the tagline
- tagline "The Heart of Property" to be placed separately
- we would like to see designs with and without personal photo, as not all agents might be placing their photos.
- Photos should not be in a box
- Name and Cell number needs to be more prominent than other details
- Design should be clean and exudes a branding of professionalism, trustworthiness and respect
For the education centre:
- Name of company is P.T. Sinar Budaya Akademi
- designs will be without photo
- name and cell number need NOT be more prominent
- design should be clean and corporate that exudes a branding of professionalism, reliability and trust
We require designs for:
- Business cards
- Open Top DL Envelopes 110mm x 220mm (plain)
- Open End DL Envelopes 110mm x 220mm (with window)
- Letter head
- Fax Cover
- 2 pocket folder with business card slot
- Open end envelopes 9 ½” x 12 ½”
Colours schemes are important to us to avoid 'clashes' with 'fengshui".
Colours allowed:
- Grey
Colours to be avoided:
- Yellow(and all other earthy colours)
- Green
- Brown(and all other woody colours)
- Red
We are open to ideas, but it should include the logo with tagline
Business card for the agency should also have the words "Buy / Sell / Lease"

```html
<!DOCTYPE html>
<html lang="en">
<head>
<meta charset="utf-8">
<title>KMT Stationery</title>
<link href="https://fonts.googleapis.com/css2?family=Lato:wght@400;700&display=swap" rel="stylesheet">
<style>
  :root{
    --backdrop:#3b3c3f;
    --paper:#f3f4f6;
    --paper-edge:#dcdee2;
    --brand:#2f6a96;
    --ink:#6f7378;
    --ink-soft:#9a9ea3;
    --faint:#e4e8ee;
  }
  *{margin:0;padding:0;box-sizing:border-box}
  html,body{width:1200px;height:672px;overflow:hidden}
  body{background:var(--backdrop);font-family:'Lato',sans-serif;position:relative}
  .sheet{position:absolute;background:var(--paper);border:1px solid var(--paper-edge);box-shadow:0 4px 14px rgba(0,0,0,.35)}
  .brand-name{font-family:'Lato',sans-serif;font-weight:700;color:var(--brand);letter-spacing:1px;display:inline-flex;align-items:center;gap:6px}
  .brand-dot{width:10px;height:10px;border-radius:50%;background:var(--brand)}
  .tiny{font-size:6px;color:var(--ink);line-height:1.5}

  /* business cards */
  .card{left:29px;width:118px;height:98px;padding:8px 8px}
  .card--front{top:372px}
  .card--back{top:482px}
  .card .brand-name{font-size:18px;margin-top:12px}
  .card__tag{font-size:5px;color:var(--ink-soft);margin-top:6px;text-align:center}
  .card--front{text-align:center}
  .card__person{font-size:6px;color:var(--ink);margin-top:3px}
  .card--back .brand-name{font-size:15px;margin-top:2px}
  .card__rule{height:1px;background:var(--paper-edge);margin:6px 0 4px}
  .card__details{font-size:4.6px;color:var(--ink);line-height:1.45}

  /* letterhead */
  .letterhead{left:180px;top:41px;width:379px;height:588px}
  .letterhead__head{position:absolute;top:26px;left:0;right:0;text-align:center}
  .letterhead .brand-name{font-size:34px}
  .letterhead__mark{position:absolute;left:120px;top:150px;width:140px;height:140px;border-radius:50%;background:var(--faint)}
  .letterhead__foot{position:absolute;bottom:20px;left:0;right:0;text-align:center;font-size:5.5px;color:var(--ink-soft);line-height:1.6}

  /* envelopes */
  .envelope{left:636px;width:538px;height:245px}
  .envelope--back{top:101px;overflow:hidden}
  .envelope--back svg{position:absolute;inset:0}
  .envelope__flap-name{position:absolute;top:56px;left:0;right:0;text-align:center}
  .envelope__flap-name .brand-name{font-size:20px}
  .envelope--front{top:362px}
  .envelope--front .envelope__logo{position:absolute;top:86px;left:0;right:0;text-align:center}
  .envelope--front .brand-name{font-size:30px}
  .envelope__foot{position:absolute;bottom:14px;left:0;right:0;text-align:center;font-size:5.5px;color:var(--ink-soft);line-height:1.6}
</style>
</head>
<body>

<section class="sheet card card--front">
  <span class="brand-name"><span class="brand-dot"></span>KMT</span>
  <p class="card__tag">The Heart of Property</p>
  <p class="card__tag">Buy / Sell / Lease</p>
</section>

<section class="sheet card card--back">
  <span class="brand-name">KMT</span>
  <div class="card__rule"></div>
  <p class="card__person">Hendra Wiratmo &middot; Owner / Realtor</p>
  <p class="card__details">
    Wisma Cakra Baruna 11 Floor, Jl. Raya Pemuda Kav. 3-4<br>
    Pasir Melati - Kebon Sirih, Jakarta Pusat - 10390<br>
    T +62 21 555 0142 &middot; K98765432<br>
    hendrawira@mailbox-example.com
  </p>
</section>

<section class="sheet letterhead">
  <div class="letterhead__head"><span class="brand-name"><span class="brand-dot"></span>KMT</span></div>
  <div class="letterhead__mark" role="img" aria-label="Faint brand watermark area"></div>
  <p class="letterhead__foot">
    P.T. Kirana Maju Teguh &middot; Wisma Cakra Baruna 11 Floor &middot; Jl. Raya Pemuda Kav. 3-4 &middot; Pasir Melati - Kebon Sirih &middot; Jakarta Pusat - 10390<br>
    T +62 21 555 0142 &middot; hendrawira@mailbox-example.com &middot; www.hendra-wiratmo-example.com
  </p>
</section>

<section class="sheet envelope envelope--back">
  <svg width="538" height="245" viewBox="0 0 538 245">
    <polyline points="0,0 269,128 538,0" fill="none" stroke="#d3d6db" stroke-width="1.5"/>
    <line x1="0" y1="245" x2="210" y2="110" stroke="#e0e2e6" stroke-width="1"/>
    <line x1="538" y1="245" x2="328" y2="110" stroke="#e0e2e6" stroke-width="1"/>
  </svg>
  <div class="envelope__flap-name"><span class="brand-name">KMT</span></div>
</section>

<section class="sheet envelope envelope--front">
  <div class="envelope__logo"><span class="brand-name"><span class="brand-dot"></span>KMT</span></div>
  <p class="envelope__foot">
    P.T. Kirana Maju Teguh &middot; Wisma Cakra Baruna 11 Floor &middot; Jl. Raya Pemuda Kav. 3-4 &middot; Jakarta Pusat - 10390<br>
    T +62 21 555 0142 &middot; www.hendra-wiratmo-example.com
  </p>
</section>

</body>
</html>
```